Intenational Rhythmic Gymnastics Frostline Trophy

We need a poster for our new annual international rhythmic gymnastics competition "Frostline Trophy". Dates are December 21 -23, 2019.Picture we would like to use is attached.We would like to see holidays colors in the poster.It should have words "international rhythmic gymnastics", Name of the competition "Frostline Trophy" and dates.Also we would like for it to say somewhere that it is in Los Angeles, California, USAIt should have information about our club on the bottom of the poster like on the file attached (hosted by Venmarra Gymnastics with logo and address and website info)We also need a flyer that ties into the poster in look and colors with empty space below so we can add directives.We would like end product to be in file format that we can edit next year when the dates change.

Target Market(s)

Rhythmic Gymnastics Clubs

Industry/Entity Type

Gym

Colors

Designer to choose colors to be used in the design.

Requirements
Must have
• Picture we uploaded and all info we requested.
• Bright holiday colors

```html
<!DOCTYPE html>
<html lang="en">
<head>
<meta charset="utf-8">
<title>Frostline Trophy Poster</title>
<link rel="stylesheet" href="https://fonts.googleapis.com/css2?family=Bebas+Neue&family=Josefin+Sans:wght@300;400;600&family=Montserrat:wght@400;600&family=Oswald:wght@300;600&display=swap">
<style>
  :root {
    --stage: #262626;
    --backdrop-top: #6e0c1b;
    --backdrop-mid: #c8182f;
    --backdrop-low: #b8142b;
    --backdrop-bottom: #560914;
    --ink: #0c3a22;
    --paper: #ffffff;
    --gold: #f4c542;
    --date-band: #1f7a3d;
    --ribbon-a: #2b2a8a;
    --ribbon-b: #4fc3d8;
    --ribbon-c: #6a3fb0;
    --skin: #d9a887;
    --leotard: #4b3a6e;
  }
  html, body {
    margin: 0;
    width: 1200px;
    height: 830px;
    overflow: hidden;
    background: var(--stage);
  }
  .canvas {
    position: relative;
    width: 1200px;
    height: 830px;
  }
  .poster {
    position: absolute;
    left: 327px;
    top: 30px;
    width: 545px;
    height: 770px;
    box-shadow: 0 6px 24px rgba(0,0,0,.5);
  }
  .club-name { font-family: "Montserrat", sans-serif; font-weight: 400; }
  .event-kicker { font-family: "Josefin Sans", sans-serif; font-weight: 300; }
  .event-discipline { font-family: "Josefin Sans", sans-serif; font-weight: 400; }
  .event-title { font-family: "Bebas Neue", sans-serif; }
  .date-month { font-family: "Oswald", sans-serif; font-weight: 300; }
  .date-days { font-family: "Oswald", sans-serif; font-weight: 600; }
  .venue-city { font-family: "Josefin Sans", sans-serif; font-weight: 600; }
  .venue-address { font-family: "Montserrat", sans-serif; font-weight: 400; }
  .venue-web { font-family: "Montserrat", sans-serif; font-weight: 600; }
</style>
</head>
<body>
<div class="canvas">
  <svg class="poster" viewBox="0 0 545 770" xmlns="http://www.w3.org/2000/svg">
    <defs>
      <linearGradient id="backdrop" x1="0" y1="0" x2="0" y2="1">
        <stop offset="0" stop-color="var(--backdrop-top)"/>
        <stop offset="0.35" stop-color="var(--backdrop-mid)"/>
        <stop offset="0.72" stop-color="var(--backdrop-low)"/>
        <stop offset="1" stop-color="var(--backdrop-bottom)"/>
      </linearGradient>
      <linearGradient id="ribbonTone" x1="0" y1="0" x2="1" y2="1">
        <stop offset="0" stop-color="var(--ribbon-a)"/>
        <stop offset="0.5" stop-color="var(--ribbon-b)"/>
        <stop offset="1" stop-color="var(--ribbon-c)"/>
      </linearGradient>
      <linearGradient id="athleteTone" x1="0" y1="0" x2="1" y2="0">
        <stop offset="0" stop-color="var(--skin)"/>
        <stop offset="0.45" stop-color="var(--leotard)"/>
        <stop offset="1" stop-color="var(--skin)"/>
      </linearGradient>
    </defs>

    <rect class="backdrop" width="545" height="770" fill="url(#backdrop)"/>

    <g class="club-mark">
      <text class="club-name" x="352" y="66" font-size="19" fill="var(--paper)" text-anchor="end">Venmarra Gymnastics</text>
      <circle cx="372" cy="60" r="9" fill="var(--gold)"/>
    </g>

    <rect class="ribbon-photo" role="img" aria-label="Blue, turquoise and purple gymnastics ribbon swirling on a stick"
          x="12" y="100" width="200" height="326" rx="90" fill="url(#ribbonTone)" opacity="0.8"/>

    <text class="event-kicker" x="502" y="150" font-size="17" letter-spacing="5.2" fill="var(--paper)" text-anchor="end">INTENATIONAL RHYTHMIC</text>
    <text class="event-discipline" x="502" y="184" font-size="34" letter-spacing="7" fill="var(--ink)" text-anchor="end">GYMNASTICS</text>

    <text class="event-title" x="78" y="388" font-size="268" textLength="420" lengthAdjust="spacingAndGlyphs" fill="var(--paper)">FROSTLINE</text>

    <rect class="athlete-photo" role="img" aria-label="Rhythmic gymnast in a jewelled purple leotard kneeling in a deep lunge, arching back and raising the ribbon stick"
          x="115" y="400" width="250" height="205" rx="40" fill="url(#athleteTone)" opacity="0.85"/>

    <text class="event-title" x="298" y="590" font-size="268" textLength="207" lengthAdjust="spacingAndGlyphs" fill="var(--ink)">TROPHY</text>

    <g class="event-dates">
      <text class="date-month" x="62" y="686" font-size="40" textLength="190" lengthAdjust="spacingAndGlyphs" fill="var(--paper)">DECEMBER</text>
      <rect x="260" y="649" width="219" height="41" fill="var(--date-band)"/>
      <text class="date-days" x="369" y="684" font-size="38" fill="var(--paper)" text-anchor="middle" letter-spacing="1">21-23, 2019</text>
    </g>

    <g class="venue">
      <text class="venue-city" x="272" y="714" font-size="12" letter-spacing="3" fill="var(--gold)" text-anchor="middle">LOS ANGELES, CALIFORNIA, USA</text>
      <text class="venue-address" x="272" y="732" font-size="9.5" fill="var(--paper)" text-anchor="middle">4820 Larkspur Avenue, #210 Westbrook, CA 91307</text>
      <text class="venue-web" x="272" y="748" font-size="11.5" letter-spacing="3" fill="var(--paper)" text-anchor="middle">www.venmarragymnastics.com</text>
    </g>
  </svg>
</div>
</body>
</html>
```